Presentation card Venture KELO - Tech Incubator from Perú

We need a Design to promote the incubator of technology Startups.
We are in Perú, we work with a string tech filter and develop enterprenurship competencies in the Startup team.
The card is to facilitators and staff memebers of VentureKELO.
We want a clear, modern, tech and agile Design.

We work to help New enterprises of technology here in Perú, we expect the candidates have a big competencies to Research and develop technological products.

We work using methodologies from QRB, Folmestry, Brakewell and Harrowgate univeesities. Our book base is the disciplina of enterpreneur.

We work events all year using diferent formats: Brightforge, Vorne price, OPRA Model Competition you can use these logros in your Design.

Set the name, role, email, cell phone number, address.

Example:
// Contact info section
Tobías Quiroveda
Swift Modeling Hub Manager
tobias.quiroveda@kelo-example.pe
(511) 999 000 417

// Address info section
VentureKELO
Technology-based business incubator
Av. Los Cedrales 884, Valdora
Lima - Perú
web: venture-kelo-example.org.pe
email: venture@kelo-example.pe
phone number: (511) 3926508 ext. 4418

// (optional)Lema section
Making happy using technology

// Social network section
facebook: venturekelooficial

Target Market(s)

Enterprenurship, CTO, Investors, Companies interested on open innovation services

Industry/Entity Type

Information Technology

Contact Information for Business Card

Name, Role, Email, Cell phone number

Colors

Designer to choose colors to be used in the design.

Requirements
Must have
• Logo forms and colors
Nice to have
• I add pictures of the leaders of incubator
Should not have
• No vertical designs

```html
<!DOCTYPE html>
<html lang="es">
<head>
<meta charset="utf-8">
<title>Venture KELO — Business Card</title>
<link href="https://fonts.googleapis.com/css2?family=Arimo:wght@400;700&display=swap" rel="stylesheet">
<style>
  :root {
    --backdrop: #e4e4e6;
    --card-white: #ffffff;
    --ink: #141414;
    --crimson: #d42a5b;
    --rule: #1a1a1a;
    --night: #050505;
    --photo-top: #c9c4bb;
    --photo-mid: #5a6360;
    --photo-low: #2b3236;
  }
  * { margin: 0; padding: 0; box-sizing: border-box; }
  html, body {
    width: 1200px; height: 864px; overflow: hidden;
    background: var(--backdrop);
    font-family: "Arimo", Arial, sans-serif;
  }
  .sheet {
    width: 1200px; height: 864px;
    display: flex; align-items: center; justify-content: center; gap: 44px;
  }
  .card {
    position: relative;
    width: 540px; height: 310px;
    border-radius: 4px;
    overflow: hidden;
    box-shadow: 0 10px 28px rgba(0,0,0,.18);
  }

  /* Front */
  .card--front { background: var(--card-white); color: var(--ink); }
  .brand {
    position: absolute; left: 0; right: 0; top: 52px;
    display: flex; align-items: center; justify-content: center; gap: 12px;
  }
  .brand__mark { width: 22px; height: 22px; background: var(--crimson); }
  .brand__name {
    font-weight: 700; font-size: 40px; letter-spacing: -0.5px;
    color: var(--ink);
  }
  .rule { position: absolute; height: 1.5px; background: var(--rule); }
  .rule--upper { left: 40px; width: 200px; top: 150px; }
  .rule--lower { left: 330px; width: 170px; top: 214px; }
  .contact {
    position: absolute; left: 0; right: 0; top: 156px;
    text-align: center;
  }
  .contact__name { font-weight: 700; font-size: 20px; color: var(--ink); }
  .contact__role { margin-top: 4px; font-size: 14px; font-weight: 700; color: var(--crimson); }
  .contact__line { margin-top: 9px; font-size: 14px; font-weight: 700; color: var(--ink); }
  .contact__line + .contact__line { margin-top: 5px; }

  /* Back */
  .card--back { background: var(--night); }
  .team-photo {
    position: absolute; left: 0; top: 0; width: 100%; height: 200px;
    background: linear-gradient(180deg, var(--photo-top) 0%, var(--photo-mid) 55%, var(--photo-low) 100%);
  }
  .back-brand {
    position: absolute; left: 0; right: 0; bottom: 38px;
    display: flex; align-items: center; justify-content: center; gap: 10px;
  }
  .back-brand__mark { width: 18px; height: 18px; background: var(--crimson); }
  .back-brand__name { font-weight: 700; font-size: 32px; color: var(--card-white); }
</style>
</head>
<body>
  <main class="sheet">
    <section class="card card--front" aria-label="Front of business card">
      <div class="brand">
        <span class="brand__mark"></span>
        <span class="brand__name">Venture KELO</span>
      </div>
      <div class="rule rule--upper"></div>
      <div class="contact">
        <p class="contact__name">Tobías Quiroveda</p>
        <p class="contact__role">Senior Software Development Engineer</p>
        <p class="contact__line">+00 410 000 2781</p>
        <p class="contact__line">tobias@kelo-example.pe</p>
      </div>
      <div class="rule rule--lower"></div>
    </section>

    <section class="card card--back" aria-label="Back of business card">
      <div class="team-photo" role="img" aria-label="Group photo of the incubator team standing together in an office in front of a projection screen"></div>
      <div class="back-brand">
        <span class="back-brand__mark"></span>
        <span class="back-brand__name">Venture KELO</span>
      </div>
    </section>
  </main>
</body>
</html>
```